Diet, Exercise, & Friends are Associated with Parkinson's disease Progression

We are researchers looking for modifiable variables associated with different rates of Parkinson's disease (PD) progression. This is a novel scale: www.VELQAN.org -- higher scores are associated with worse quality of life. Low is good. High is bad. Each of the dots is a real person (maybe those should disappear?). The line represents the typical rate of PD progression over time. Color scheme of different degrees of quality of life can change, but the general concept seems to be working. (see updated version at the bottom of the www.VELQAN.org website)We need to combine the exercise data from here. This poster was essentially my attempt at an infographic for scientists:https://files.brindlehost.net/static/7a2c91e0b4/t/3d8e55f1a0/1482209931245/TRX2017+Meals.pdf. The updated data is in the uploaded figure below. Please use this list/ verbage!I don't necessarily need to stick to red=bad, green=good, but that's the best I've been able to come up with to communicate all this. I can get the actual data output later, but it might be nice to be able to demonstrate intensity. Veggies are quite a bit better than spices. Loneliness is much, much worse than pasta. This is the original published data. We have updated data and want to turn it into an infographic (while we work on a new manuscript).https://www.quorvelpress.com/journals/jcrt/2017/8127439/
Target Market(s)
Individuals age 40-80 with Parkinson's disease (and their friends & family members).
Neurologists should be handing this out in their offices.
When patients ask their physician about nutrition, etc., we want this to be the 1-pg handout they give them.
Industry/Entity Type
Medicine
Font styles to use
Colors
Designer to choose colors to be used in the design.
Requirements
Must have
- VEL-QAN scale (www.VELQAN.org)-- use this picture on top. OK to change color.
- Lists foods/ activities associated with different rates of progression
- Title: "Food, Friends, and Exercise: Lifestyle Associations with PD Progression"
- Legend/ disclaimer (smaller font):
- "All results were adjusted for age, gender, and years since diagnosis. Total sample size: 1600+
- Based on the methods described in publication: "Effects of Meal Timing and Herbal Intake on Tremor Course" [Orvanto TJ et al, Clin Neuro Rehab Rev 2017], an updated analysis was performed on data on 7 May 2019. (N >1600)"
- "VEL-QAN scores available at www.VELQAN.org"
- Must fit on a single 8.5 x 11" page.
Nice to have
- The background should be white-- I want neurologists/ physicians downloading it, printing it, and distributing to patients. I don't want to waste ink.
- Logo for Kellworth University and/or the logo for the "HOLT Path MX" Study. I like the KU emblem in one corner and the picture at the top of this website: www.VELQAN.org
- Would be nice if it could be understood between cultures and/ or easily translated.
- Would be nice if we could invite people to participate in the study!
- "To learn about joining the study, please to www.HOLTPathMX.kellworth.edu"
Should not have
- Pictures of overweight people, or the impression that a muscular white guy is the ideal. I want to leave room for diversity and flexible interpretation.
- Too much text- a good-sized portion of this group will have poor vision and/or dementia. Needs to be simple.
- I like the simplicity of "Good" and "Bad"... don't love the labels. Seems to 'jugdgy'. Maybe "Encourage" and "Avoid" OR "Positive" and "Negative"

```html
<!DOCTYPE html>
<html lang="en">
<head>
<meta charset="utf-8">
<title>VEL-QAN Scale – Quality of Life</title>
<link href="https://fonts.googleapis.com/css2?family=Poppins:wght@500;600;700&display=swap" rel="stylesheet">
<style>
  :root{
    --brand-red:#A0372A;
    --poor:#A96853;
    --fair:#E2A762;
    --good:#8AA0CA;
    --excellent:#A5C972;
    --avoid:#B06A5A;
    --avoid-icon:#B5775A;
    --encourage:#9CC96C;
    --ink:#1d1d1d;
    --paper:#ffffff;
  }
  *{box-sizing:border-box;margin:0;padding:0}
  html,body{width:1200px;height:936px;overflow:hidden;background:var(--paper)}
  body{font-family:"Poppins",sans-serif;color:var(--ink);position:relative}
  .frame{position:absolute;left:10px;top:16px;width:1174px;height:902px;border:2px solid var(--brand-red);border-radius:20px}
  .title{position:absolute;left:0;width:1024px;text-align:center;color:var(--brand-red);font-weight:700;font-size:32px;line-height:1}
  .title--main{top:38px}
  .title--scale{top:75px}
  .society{position:absolute;left:990px;top:34px;width:170px;text-align:center;color:var(--brand-red);font-weight:500;font-size:10.5px;line-height:1.3}
  .society__mark{display:block;width:50px;height:50px;border-radius:50%;background:var(--brand-red);opacity:.35;margin:0 auto 8px}
  .chart{position:absolute;left:0;top:0}
  .legend-row{position:absolute;left:838px;font-weight:600;font-size:16px;line-height:1;white-space:nowrap}
  .legend-row::before{content:"";display:inline-block;width:9px;height:9px;border-radius:50%;margin-right:7px;vertical-align:2px;background:var(--dot)}
  .avoid{--dot:var(--avoid)}
  .encourage{--dot:var(--encourage)}
  .footnote{position:absolute;left:0;width:1200px;top:891px;text-align:center;font-size:13.5px;font-weight:600}
</style>
</head>
<body>
<div class="frame"></div>

<h1 class="title title--main">Patient-Reported Outcomes in Parkinson’s Disease</h1>
<h2 class="title title--scale">VEL-QAN SCALE</h2>

<div class="society"><span class="society__mark"></span>Meridian Tremor and Motion Research Society</div>

<svg class="chart" width="1200" height="936" viewBox="0 0 1200 936" font-family="Poppins, sans-serif">
  <defs>
    <g id="fork-icon" fill="none" stroke="#fff" stroke-linecap="round">
      <path d="M-4 -14 V-4 Q-4 1 0 1 Q4 1 4 -4 V-14 M0 -14 V1" stroke-width="2.2"/>
      <line x1="0" y1="1" x2="0" y2="17" stroke-width="3.2"/>
    </g>
    <g id="knife-icon">
      <path d="M-1.6 2 L-1.6 -16 Q4.5 -9 2.4 2 Z" fill="#fff"/>
      <line x1="0" y1="2" x2="0" y2="17" stroke="#fff" stroke-width="3.6" stroke-linecap="round"/>
    </g>
  </defs>

  <text x="586" y="162" text-anchor="middle" font-size="27" font-weight="600" fill="#1d1d1d">Quality of Life</text>
  <!-- bands -->
  <rect x="138" y="176" width="600" height="246" fill="var(--poor)"/>
  <rect x="138" y="422" width="600" height="124" fill="var(--fair)"/>
  <rect x="138" y="546" width="600" height="123" fill="var(--good)"/>
  <rect x="138" y="669" width="600" height="123" fill="var(--excellent)"/>
  <!-- grid -->
  <g stroke="#fff" stroke-width="1.5">
    <line x1="249" y1="176" x2="249" y2="792"/>
    <line x1="360" y1="176" x2="360" y2="792"/>
    <line x1="470" y1="176" x2="470" y2="792"/>
    <line x1="581" y1="176" x2="581" y2="272"/>
    <line x1="581" y1="318" x2="581" y2="492"/>
    <line x1="581" y1="536" x2="581" y2="590"/>
    <line x1="581" y1="630" x2="581" y2="700"/>
    <line x1="581" y1="745" x2="581" y2="792"/>
    <line x1="692" y1="176" x2="692" y2="792"/>
    <line x1="138" y1="299" x2="520" y2="299"/>
    <line x1="644" y1="299" x2="738" y2="299"/>
    <line x1="138" y1="422" x2="738" y2="422"/>
    <line x1="138" y1="669" x2="738" y2="669"/>
  </g>
  <line x1="138" y1="546" x2="738" y2="546" stroke="#222" stroke-width="1.5"/>
  <!-- trend band -->
  <polygon points="145,634 738,339 738,425" fill="#fff" opacity="0.72"/>
  <line x1="145" y1="634" x2="738" y2="385" stroke="var(--poor)" stroke-width="3.5" stroke-dasharray="11 6"/>
  <rect x="138" y="176" width="600" height="616" fill="none" stroke="var(--poor)" stroke-width="2"/>
  <!-- band labels -->
  <g fill="#fff" font-weight="600" font-size="29" text-anchor="middle">
    <text x="583" y="304">Poor</text>
    <text x="586" y="522">Fair</text>
    <text x="583" y="620">Good</text>
    <text x="583" y="734">Excellent</text>
  </g>
  <!-- axes -->
  <g font-size="18" font-weight="700" fill="#1d1d1d" text-anchor="end">
    <text x="126" y="183">2,500</text>
    <text x="126" y="305">2,000</text>
    <text x="126" y="429">1,500</text>
    <text x="126" y="553">1,000</text>
    <text x="118" y="676">500</text>
    <text x="118" y="799">0</text>
  </g>
  <g font-size="18" font-weight="700" fill="#1d1d1d" text-anchor="middle">
    <text x="138" y="820">0</text>
    <text x="249" y="820">5</text>
    <text x="360" y="820">10</text>
    <text x="470" y="820">15</text>
    <text x="581" y="820">20</text>
    <text x="692" y="820">25</text>
  </g>
  <text x="426" y="853" text-anchor="middle" font-size="20" font-weight="700" fill="#1d1d1d">Years Since Diagnosis</text>
  <text transform="translate(51 484) rotate(-90)" text-anchor="middle" font-size="20" font-weight="700" fill="#1d1d1d">VEL-QAN Score</text>

  <!-- avoid icons -->
  <g fill="var(--avoid-icon)">
    <circle cx="788" cy="198" r="13"/>
    <path d="M762 236 q0 -22 26 -22 q26 0 26 22 z"/>
    <circle cx="788" cy="304" r="27"/>
    <path d="M762 362 q0 -12 13 -12 q13 0 13 12 q0 -12 13 -12 q13 0 13 12 q0 16 -26 30 q-26 -14 -26 -30 z"/>
  </g>
  <use href="#fork-icon" transform="translate(788 304) rotate(40)"/>
  <use href="#knife-icon" transform="translate(788 304) rotate(-40)"/>
  <polyline points="764,374 778,374 783,366 789,382 794,370 812,370" fill="none" stroke="#fff" stroke-width="2" stroke-linecap="round"/>

  <!-- encourage icons -->
  <g fill="var(--encourage)">
    <circle cx="788" cy="558" r="13"/>
    <path d="M762 596 q0 -22 26 -22 q26 0 26 22 z"/>
    <circle cx="788" cy="669" r="27"/>
    <path d="M762 748 q0 -12 13 -12 q13 0 13 12 q0 -12 13 -12 q13 0 13 12 q0 16 -26 30 q-26 -14 -26 -30 z"/>
  </g>
  <use href="#fork-icon" transform="translate(788 669) rotate(40)"/>
  <use href="#knife-icon" transform="translate(788 669) rotate(-40)"/>
  <polyline points="764,760 778,760 783,752 789,768 794,756 812,756" fill="none" stroke="#fff" stroke-width="2" stroke-linecap="round"/>
</svg>

<div class="legend-row avoid" style="top:199px">“I’m overweight.”</div>
<div class="legend-row avoid" style="top:219px">“I’m lonely.”</div>

<div class="legend-row avoid" style="top:273px">Dairy</div>
<div class="legend-row avoid" style="top:292px">Beef</div>
<div class="legend-row avoid" style="top:310px">Chicken</div>
<div class="legend-row avoid" style="top:329px">Soda</div>
<div class="legend-row avoid" style="top:273px;left:940px">Fried foods</div>
<div class="legend-row avoid" style="top:292px;left:940px">Canned fruits</div>
<div class="legend-row avoid" style="top:310px;left:940px">Canned vegetables</div>
<div class="legend-row avoid" style="top:329px;left:940px">Frozen vegetables</div>

<div class="legend-row avoid" style="top:371px">No benefit associated to</div>
<div class="legend-row" style="top:390px;left:854px">0-2 days/week of exercise</div>

<div class="legend-row encourage" style="top:546px">“I have lots of friends.”</div>
<div class="legend-row encourage" style="top:566px">“I try to eat organic when possible.”</div>
<div class="legend-row encourage" style="top:586px">“I cook most of my own meals.”</div>

<div class="legend-row encourage" style="top:634px">Fresh vegetables</div>
<div class="legend-row encourage" style="top:653px">Olive &amp; coconut oil</div>
<div class="legend-row encourage" style="top:671px">Nuts &amp; seeds</div>
<div class="legend-row encourage" style="top:690px">Non-fried fish</div>
<div class="legend-row encourage" style="top:632px;left:1028px">Fresh fruit</div>
<div class="legend-row encourage" style="top:650px;left:1028px">Fresh herbs</div>
<div class="legend-row encourage" style="top:669px;left:1028px">Spices</div>
<div class="legend-row encourage" style="top:687px;left:1028px">Wine</div>

<div class="legend-row encourage" style="top:740px">7 d/w of exercise is better than 6</div>
<div class="legend-row encourage" style="top:758px">6 d/wk of exercise is better than 5…</div>
<div class="legend-row encourage" style="top:777px">Trend continues to 3d/wk</div>

<p class="footnote">All results adjusted for age, gender, and years since diagnosis. Total sample size: 1600+. Updated dataset as of 7 May 2019.</p>
</body>
</html>
```